Redesign of Smart Watch Gift Voucher-SEE ATTACHED CURRENT DESIGN

I need to redesign my existing design using all same content and elements.

MY ENVISION: I invision more of a professional advertisement type of flyer/voucher. Imagine how Quorrel.com would create a professionally looking flyer promoting the tavix or tavun.

you can get many ideas about professional design by looking at some of quorrels flyer designs :
https://www.findlery.example/search?q=tavix+advertisment&tbm=isch

stock photos are attached, you do not have to use them all, you can use some or none i am open to your designs using your own images if you want...just make sure the smartwatch looks black

DO NOT LEAVE ANY CONTENT OR ELEMENTS OUT ON MOCK UP PLEASE

SEE ATTACHED CURRENT DESIGN

I need to redesign my existing design using all same content and elements. DO NOT LEAVE ANY CONTENT OR ELEMENTS OUT ON MOCK UP PLEASE

Target Market(s)

B2B-you can get many ideas about professional design by looking at some of quorrels flyer designs :

Industry/Entity Type

Marketing

Requirements
Must have
• I need to redesign my existing design using all same content and elements. DO NOT LEAVE ANY CONTENT OR ELEMENTS OUT ON MOCK UP PLEASE

Nice to have

Should not have

```html
<!DOCTYPE html>
<html lang="en">
<head>
<meta charset="utf-8">
<title>Smart Fitness Watch Certificate</title>
<link href="https://fonts.googleapis.com/css2?family=Jost:wght@200;300;400;500;600&display=swap" rel="stylesheet">
<style>
  :root{
    --bg:#0d0d0e;
    --ink:#ffffff;
    --red:#d8232a;
    --band-red:#e21f26;
    --grey:#d9d9d9;
    --dash:#6a1a1c;
  }
  *{margin:0;padding:0;box-sizing:border-box}
  html,body{width:927px;height:1200px;overflow:hidden;background:var(--bg)}
  body{font-family:"Jost",sans-serif;color:var(--ink);position:relative}
  .abs{position:absolute}
  .center{left:0;width:927px;text-align:center}

  .hero-title{top:62px;font-size:96px;font-weight:200;letter-spacing:2px;line-height:1}
  .hero-sub{top:162px;font-size:31px;font-weight:300;color:var(--red);letter-spacing:1px}

  .section-head{font-size:24px;font-weight:300;color:var(--red);line-height:29px;letter-spacing:1px}
  .left-col{left:61px;width:200px}
  .body-copy{font-size:10.6px;line-height:13.6px;font-weight:300}
  .how-head{top:251px}
  .how-copy{top:321px}
  .say-head{top:538px}
  .quote{top:605px}
  .quote-name{top:655px;font-size:9.8px;color:var(--red);font-weight:400;letter-spacing:.3px}

  .watch-hero{left:330px;top:252px;width:276px;height:420px}

  .features-head{left:710px;top:256px}
  .feature-list{left:711px;top:318px;list-style:none}
  .feature-list li{display:flex;align-items:center;height:30.4px;font-size:12px;font-weight:300;letter-spacing:.2px}
  .feature-list svg{width:10px;height:10px;margin-right:8px;flex:none}

  .tagline{top:724px;font-size:32px;font-weight:300;color:var(--red);line-height:38.5px;letter-spacing:.5px}

  .rule{left:84px;width:760px;border-top:1px dashed var(--dash)}
  .rule-top{top:821px}
  .rule-bottom{top:873px}
  .exclusive{top:832px;font-size:26px;font-weight:300;letter-spacing:1px;display:flex;justify-content:center;align-items:center;gap:0}
  .exclusive .lbl{width:300px;text-align:right}
  .exclusive .arrows{width:110px;display:flex;justify-content:center}
  .exclusive .name{width:300px;text-align:left}

  .congrats{top:889px;font-size:14.6px;font-weight:500;line-height:18.4px;letter-spacing:.3px}
  .details{top:935px;font-size:11.2px;font-weight:300;line-height:15.3px;left:130px;width:667px}

  .cert{left:58px;top:1005px;width:812px;height:119px;background:var(--grey);overflow:hidden}
  .cert-red{position:absolute;inset:0}
  .cert-frame{position:absolute;left:9px;top:9px;right:9px;bottom:9px;border:1px dashed #7a7a7a}
  .cert-frame.on-red{border-color:rgba(255,255,255,.45)}
  .cert-text{position:absolute;font-size:11.8px;font-weight:300;line-height:15.5px;letter-spacing:.3px}
  .cert-text b{font-weight:500;letter-spacing:.8px}
  .cert-divider{position:absolute;width:1px;background:rgba(255,255,255,.75)}
  .cert-id{left:28px;top:21px}
  .cert-exp{left:28px;top:73px}
  .cert-view{left:160px;top:21px}
  .cert-url{left:160px;top:72px}
  .cert-url b{font-size:12.4px;letter-spacing:1px}
  .cert-url small{display:block;font-size:8.2px;line-height:12px}
  .cert-watch{position:absolute;top:14px;width:86px;height:92px}

  .footer{top:1139px;font-size:15px;font-weight:300;letter-spacing:.5px;display:flex;align-items:center;left:73px}
  .footer .lbl{width:380px}
  .footer .arrows{width:140px;display:flex;justify-content:center}
</style>
</head>
<body>

<h1 class="abs center hero-title">ENJOY</h1>
<p class="abs center hero-sub">Your Brand New Smart Fitness watch</p>

<h2 class="abs left-col section-head how-head">HOW CAN<br>WE DO THIS?</h2>
<p class="abs left-col body-copy how-copy">We Have A Couple Retial Parters That We Team Up With To “Crowd Purchase” Huge Shipping Containers That Hold 10’s Of Thousands Of Electronic Products At 80-90% Off Retail. We Simply Pass Our Savings On To You As We Do Not Profit From Our Electronic Products. You Are Basically Able To “Piggy Back” On Our Parternships And Buying Power To Get An Attractive Electronic Premimum For A Fraction Of The Retail Cost.</p>

<h2 class="abs left-col section-head say-head">WHAT<br>OTHERS SAY?</h2>
<p class="abs left-col body-copy quote">“Are You Sure This Is Not A Norvane Pulse Smartwatch In Disguise??? I Love Mine”.</p>
<p class="abs left-col quote-name">MARCO T. HARBOR POINT, NJ</p>

<svg class="abs watch-hero" viewBox="0 0 276 420" role="img" aria-label="Product photo of the black round smart fitness watch with silicone strap">
  <defs>
    <radialGradient id="face" cx="50%" cy="45%" r="60%">
      <stop offset="0" stop-color="#2c2e31"/>
      <stop offset="1" stop-color="#0c0c0d"/>
    </radialGradient>
  </defs>
  <rect x="68" y="0" width="140" height="420" rx="18" fill="#1c1c1e"/>
  <circle cx="138" cy="210" r="132" fill="#202123"/>
  <circle cx="138" cy="210" r="120" fill="url(#face)"/>
</svg>

<h2 class="abs section-head features-head">FEATURES</h2>
<ul class="abs feature-list">
  <li><svg viewBox="0 0 10 10"><circle cx="5" cy="5" r="4.2" fill="none" stroke="#d8232a" stroke-width="1"/><path d="M3 5.2l1.5 1.4L7.3 3.6" fill="none" stroke="#d8232a" stroke-width="1"/></svg>Pedomoter</li>
  <li><svg viewBox="0 0 10 10"><circle cx="5" cy="5" r="4.2" fill="none" stroke="#d8232a" stroke-width="1"/><path d="M3 5.2l1.5 1.4L7.3 3.6" fill="none" stroke="#d8232a" stroke-width="1"/></svg>Calorie Counter</li>
  <li><svg viewBox="0 0 10 10"><circle cx="5" cy="5" r="4.2" fill="none" stroke="#d8232a" stroke-width="1"/><path d="M3 5.2l1.5 1.4L7.3 3.6" fill="none" stroke="#d8232a" stroke-width="1"/></svg>Blood Pressure Monitor</li>
  <li><svg viewBox="0 0 10 10"><circle cx="5" cy="5" r="4.2" fill="none" stroke="#d8232a" stroke-width="1"/><path d="M3 5.2l1.5 1.4L7.3 3.6" fill="none" stroke="#d8232a" stroke-width="1"/></svg>Sleep Monitoring</li>
  <li><svg viewBox="0 0 10 10"><circle cx="5" cy="5" r="4.2" fill="none" stroke="#d8232a" stroke-width="1"/><path d="M3 5.2l1.5 1.4L7.3 3.6" fill="none" stroke="#d8232a" stroke-width="1"/></svg>Reminders Feature</li>
  <li><svg viewBox="0 0 10 10"><circle cx="5" cy="5" r="4.2" fill="none" stroke="#d8232a" stroke-width="1"/><path d="M3 5.2l1.5 1.4L7.3 3.6" fill="none" stroke="#d8232a" stroke-width="1"/></svg>Alarm Clock</li>
  <li><svg viewBox="0 0 10 10"><circle cx="5" cy="5" r="4.2" fill="none" stroke="#d8232a" stroke-width="1"/><path d="M3 5.2l1.5 1.4L7.3 3.6" fill="none" stroke="#d8232a" stroke-width="1"/></svg>Distance Tracker</li>
  <li><svg viewBox="0 0 10 10"><circle cx="5" cy="5" r="4.2" fill="none" stroke="#d8232a" stroke-width="1"/><path d="M3 5.2l1.5 1.4L7.3 3.6" fill="none" stroke="#d8232a" stroke-width="1"/></svg>Heart Rate Monitor</li>
  <li><svg viewBox="0 0 10 10"><circle cx="5" cy="5" r="4.2" fill="none" stroke="#d8232a" stroke-width="1"/><path d="M3 5.2l1.5 1.4L7.3 3.6" fill="none" stroke="#d8232a" stroke-width="1"/></svg>Stopwatch</li>
  <li><svg viewBox="0 0 10 10"><circle cx="5" cy="5" r="4.2" fill="none" stroke="#d8232a" stroke-width="1"/><path d="M3 5.2l1.5 1.4L7.3 3.6" fill="none" stroke="#d8232a" stroke-width="1"/></svg>Phone Locator</li>
  <li><svg viewBox="0 0 10 10"><circle cx="5" cy="5" r="4.2" fill="none" stroke="#d8232a" stroke-width="1"/><path d="M3 5.2l1.5 1.4L7.3 3.6" fill="none" stroke="#d8232a" stroke-width="1"/></svg>Remote Camera</li>
  <li><svg viewBox="0 0 10 10"><circle cx="5" cy="5" r="4.2" fill="none" stroke="#d8232a" stroke-width="1"/><path d="M3 5.2l1.5 1.4L7.3 3.6" fill="none" stroke="#d8232a" stroke-width="1"/></svg>Waterproof</li>
</ul>

<p class="abs center tagline">Take Control Of Your Life With Your<br>New Smart Fitness Watch Powered By Bluetooth</p>

<div class="abs rule rule-top"></div>
<div class="abs center exclusive">
  <span class="lbl">EXCLUSIVELY FOR</span>
  <span class="arrows"><svg width="30" height="14" viewBox="0 0 30 14"><path d="M1 1l6 6-6 6M10 1l6 6-6 6M19 1l6 6-6 6" fill="none" stroke="#d8232a" stroke-width="1.4"/></svg></span>
  <span class="name">ELLIOT RANSFORD</span>
</div>
<div class="abs rule rule-bottom"></div>

<p class="abs center congrats">Congratulations, you hove been rewarded with a Brand New Smart Fitness Watch<br>Powered by Bluetooth shipped right to your door.</p>
<p class="abs details" style="text-align:center">Just pay shipping and handling. Your new Smart Fitness Watch has these features: Sport Mode, Pedomoter, distance, calorie counter,&nbsp; heart rate, blood pressure, stopwatch, sleep monitoring, phone locator, reminders, remote camera, an alarm clock and much more!</p>

<div class="abs cert">
  <svg class="cert-red" viewBox="0 0 812 119" preserveAspectRatio="none"><polygon points="0,0 454,0 506,119 0,119" fill="#e21f26"/></svg>
  <div class="cert-frame"></div>
  <div class="cert-text cert-id">CERTIFICATE ID<br><b>91772-89218</b></div>
  <div class="cert-text cert-exp">EXPIRES<br><b>10/03/2020</b></div>
  <div class="cert-divider" style="left:141px;top:22px;height:33px"></div>
  <div class="cert-divider" style="left:141px;top:71px;height:33px"></div>
  <div class="cert-text cert-view">VIEW ALL THE DETAILS OF THIS<br>SPECIAL OFFER AND REDEEM ONLINE AT</div>
  <div class="cert-text cert-url"><b>WWW.PERKSANDGIFTVAULT.COM</b><small>*TERMS AND CONDITIONS APPLY SEE WEBSITE FOR DETAILS</small></div>
  <svg class="cert-watch" style="left:510px" viewBox="0 0 86 92" role="img" aria-label="Photo of black smart watch, angled view"><rect x="22" y="2" width="42" height="88" rx="8" fill="#2a2a2c"/><circle cx="43" cy="46" r="34" fill="#1a1a1c"/></svg>
  <svg class="cert-watch" style="left:606px" viewBox="0 0 86 92" role="img" aria-label="Photo of black smart watch, front view"><rect x="22" y="2" width="42" height="88" rx="8" fill="#2a2a2c"/><circle cx="43" cy="46" r="34" fill="#1a1a1c"/></svg>
  <svg class="cert-watch" style="left:706px" viewBox="0 0 86 92" role="img" aria-label="Photo of black smart watch, side view"><rect x="22" y="2" width="42" height="88" rx="8" fill="#2a2a2c"/><circle cx="43" cy="46" r="34" fill="#1a1a1c"/></svg>
</div>

<div class="abs footer">
  <span class="lbl">THIS CERTIFICATE IS COMPLIMENTS OF</span>
  <span class="arrows"><svg width="26" height="13" viewBox="0 0 26 13"><path d="M1 1l5.5 5.5L1 12M9.5 1l5.5 5.5L9.5 12M18 1l5.5 5.5L18 12" fill="none" stroke="#d8232a" stroke-width="1.3"/></svg></span>
  <span class="name">Your Company Name Here</span>
</div>

</body>
</html>
```